Real estate company needs a letterhead design

A young real estate company needs a letterhead / stationery design, it should include the company's logo. It should look exactly the same as on the business cards. (With the phrase "a brand of FEO Immobilien & Projektentwicklung GmbH")

In addition, it should also include the 4 round seals.

color code blue # 00456b gray # 333333

Word and PDF are welcome.

FEO Immobilien & Projektentwicklung GmbH
Managing director: Mag. Lukas Strenhofer
Anton-Wiesmayr-Strasse 3c / 41
6300 Wörgl

Tel .: +436645917283
Email: office@wohnquell.example
Web: www.wohnquell.example

Sparkasse Almhofen, Bergländer Sparkasse from 1893, Gildenkasse
Ferdinand-Moosrainer-Strasse 9, 6300 Wörgl
IBAN: AT31 4819 2093 5521 6604
BIC: GLMRAT31XXX
Account holder: FEO Immobilien & Projektentwicklung GmbH

FN: XXXXXXX
UID: XXXXXXX

```html
<!DOCTYPE html>
<html lang="en">
<head>
<meta charset="utf-8">
<title>Wohnquell Letterhead</title>
<link href="https://fonts.googleapis.com/css2?family=Montserrat:wght@400;600;800&display=swap" rel="stylesheet">
<style>
  :root {
    --brand-blue: #00456b;
    --text-gray: #333333;
    --seal-red: #e8472a;
    --backdrop: #e9e9ea;
    --paper: #ffffff;
  }
  * { box-sizing: border-box; margin: 0; padding: 0; }
  html, body {
    width: 1200px;
    height: 1029px;
    overflow: hidden;
    background: var(--backdrop);
    font-family: "Montserrat", sans-serif;
  }
  .letterhead {
    position: absolute;
    left: 253px;
    top: 24px;
    width: 694px;
    height: 981px;
    background: var(--paper);
    box-shadow: 0 6px 24px rgba(0,0,0,0.12);
  }
  .brand-name {
    position: absolute;
    left: 56px;
    top: 86px;
    font-size: 27px;
    font-weight: 800;
    letter-spacing: 0.5px;
    color: var(--brand-blue);
    display: flex;
    align-items: center;
    gap: 8px;
  }
  .brand-name .brand-dot {
    width: 9px;
    height: 9px;
    background: var(--brand-blue);
    display: inline-block;
  }
  .company-details {
    position: absolute;
    left: 300px;
    top: 66px;
    font-size: 8.6px;
    line-height: 1.42;
    color: var(--text-gray);
  }
  .company-details .company-title {
    font-weight: 600;
    color: var(--brand-blue);
  }
  .company-details .gap { height: 9px; }
  .company-details .label { color: var(--brand-blue); }
  .footer-contacts {
    position: absolute;
    right: 58px;
    top: 800px;
    display: flex;
    gap: 26px;
    font-size: 11px;
    color: var(--text-gray);
  }
  .footer-contacts .contact-item {
    display: flex;
    align-items: center;
    gap: 5px;
  }
  .footer-contacts svg { width: 9px; height: 9px; fill: var(--brand-blue); }
  .footer-rule {
    position: absolute;
    left: 56px;
    right: 56px;
    top: 822px;
    height: 1.5px;
    background: var(--brand-blue);
  }
  .seal-row {
    position: absolute;
    right: 70px;
    top: 840px;
    display: flex;
    gap: 38px;
  }
  .seal {
    width: 56px;
    height: 56px;
    border-radius: 50%;
    border: 1.5px solid var(--seal-red);
    display: flex;
    align-items: center;
    justify-content: center;
  }
  .seal::after {
    content: "";
    width: 30px;
    height: 30px;
    border-radius: 50%;
    background: var(--seal-red);
  }
</style>
</head>
<body>
  <main class="letterhead">
    <div class="brand-name"><span class="brand-dot"></span>WOHNQUELL</div>

    <section class="company-details">
      <div class="company-title">FEO Immobilien &amp; Projektentwicklung GmbH</div>
      <div>Managing director: Mag. Lukas Strenhofer</div>
      <div>Anton-Wiesmayr-Strasse 3c / 41</div>
      <div>6300 Wörgl</div>
      <div class="gap"></div>
      <div>Sparkasse Almhofen, Bergländer Sparkasse from 1893,</div>
      <div>Gildenkasse</div>
      <div>Ferdinand-Moosrainer-Strasse 9, 6300 Wörgl</div>
      <div><span class="label">IBAN:</span> AT31 4819 2093 5521 6604</div>
      <div><span class="label">BIC:</span> GLMRAT31XXX</div>
      <div><span class="label">Account holder:</span> FEO Immobilien &amp; Projektentwicklung GmbH</div>
      <div><span class="label">FN:</span> XXXXXXX</div>
      <div><span class="label">UID:</span> XXXXXXX</div>
    </section>

    <footer>
      <div class="footer-contacts">
        <span class="contact-item">
          <svg viewBox="0 0 24 24" aria-hidden="true"><path d="M6.6 10.8a15.1 15.1 0 0 0 6.6 6.6l2.2-2.2a1 1 0 0 1 1-.25 11.4 11.4 0 0 0 3.6.57 1 1 0 0 1 1 1V20a1 1 0 0 1-1 1A17 17 0 0 1 3 4a1 1 0 0 1 1-1h3.5a1 1 0 0 1 1 1c0 1.25.2 2.45.57 3.57a1 1 0 0 1-.25 1z"/></svg>
          +436645917283
        </span>
        <span class="contact-item">
          <svg viewBox="0 0 24 24" aria-hidden="true"><path d="M2 5h20v14H2z M2 5l10 8 10-8" /></svg>
          office@wohnquell.example
        </span>
        <span class="contact-item">
          <svg viewBox="0 0 24 24" aria-hidden="true"><circle cx="12" cy="12" r="10"/></svg>
          www.wohnquell.example
        </span>
      </div>
      <div class="footer-rule"></div>
      <div class="seal-row">
        <div class="seal" role="img" aria-label="Certification seal"></div>
        <div class="seal" role="img" aria-label="Certification seal"></div>
        <div class="seal" role="img" aria-label="Certification seal"></div>
        <div class="seal" role="img" aria-label="Certification seal"></div>
      </div>
    </footer>
  </main>
</body>
</html>
```